依頼詳細
下記ブランドコンセプトに沿ったご提案をお願い致します。
プロトタイプを添付いたします。構成等、より優れていると思えるご提案がありましたら無視して頂いて構いません。
ブランドコンセプトは以下の通りです。

-- 以下、ブランドコンセプト
「自然が持つ美しさ」と「暮らす人の思い」を取り入れ『生活が楽しい住まい』を創ります
人々に永く愛されてきた天然素材を使用することで自然素材だけが持つ色や質感から確かな手触りと温もりを暮らす人に与え続けてくれます。新しいだけを追い過ぎず自然素材の持つ機能性を生かして自然の働きでしっかりと家を守る
それは流行に左右されない気品を保つ「素朴で美しい風合い」に仕上がります。

住む人のライフスタイルや好みをしっかりとお聞かせいただいた上で土地を生かし隣地環境と調和のある設計を企画し、その人らしい家を一緒に考えていきます。
それはその人がどんなふうに暮らしていきたいのかを一緒に考え、その地で永く暮らしていくイメージを膨らませ生活が楽しくなる様な空間を提案します。
-- 以上、ブランドコンセプト
サイトURL
http://tovaru.com/
ページ数
1ページ
希望イメージ
シンプル 複雑
単色 カラフル
暗い 明るい
日常 高級
遊び心 厳粛
未来的 伝統的
女性的 男性的
希望する色
納品ファイル
補足説明
トップページに関するプロトタイプを「トップページ.png」として添付しております。
また、素材として利用可能なものは下記dropboxリンクよりご利用ください。
https://www.filoshare-box.net/s/7kq2mz/sample-assets

■ 選んだ理由

全員が色使いやコンテンツの配置などを理由として同デザインを選択しました。
似通ったデザインの中でも全員の目を引く、魅力的な部分があったのだと考えます。

■ 提案者全員のお礼・コメント

今回は多くの皆様に貴重なお時間を使って頂きご提案頂きました事、大変うれしく思い感謝申し上げます。
複数名で選考を行いましたが、選考するメンバー全員でどれも素晴らしいデザインだよねと口をそろえて申しておりました。

本当にありがとうございました。

```html
<!DOCTYPE html>
<html lang="ja">
<head>
<meta charset="utf-8">
<title>Tovaru | 自然素材の家づくり</title>
<link rel="stylesheet" href="https://fonts.googleapis.com/css2?family=Noto+Sans+JP:wght@400;500;700&family=Noto+Serif+JP:wght@500;700&display=swap">
<style>
:root{
  --brown:#2b1f18;
  --cream:#f6f0e5;
  --paper:#fbf8f2;
  --gold:#d8b46a;
  --gold-dark:#b38d43;
  --red:#b3262c;
  --red-dark:#7d1a1e;
  --blue:#5b79bd;
  --ink:#3b2f27;
  --muted:#8d7c6c;
  --white:#ffffff;
}
*{box-sizing:border-box;margin:0;padding:0}
html,body{width:1200px;height:2500px;overflow:hidden}
body{background:var(--paper);color:var(--ink);font-family:"Noto Sans JP",sans-serif;position:relative}

/* Header / hero */
.topbar{position:absolute;top:0;left:0;width:1200px;height:24px;background:var(--brown);color:#d8cbb9;font-size:11px;line-height:24px;text-align:right;padding-right:20px;z-index:2}
.hero{position:absolute;top:0;left:0;width:1200px;height:620px;background:linear-gradient(180deg,#9fb6cb 0%,#c9d6e1 38%,#e8e4dc 60%,#7e7a6c 86%,#5f6a4c 100%)}
.logo-box{position:absolute;top:26px;left:22px;width:112px;height:112px;background:var(--white);display:flex;flex-direction:column;align-items:center;justify-content:center;gap:6px;z-index:3}
.logo-box .mark{width:16px;height:16px;border-radius:50%;background:var(--gold)}
.logo-box .name{font-family:"Noto Serif JP",serif;font-weight:700;font-size:20px;color:var(--gold-dark);letter-spacing:1px}
.tel-box{position:absolute;top:30px;right:12px;width:250px;height:56px;background:rgba(43,31,24,.92);color:var(--white);display:flex;align-items:center;gap:10px;padding:0 14px;z-index:3}
.tel-box .label{font-size:9px;color:#d8cbb9;line-height:1.3}
.tel-box .num{font-size:24px;font-weight:700;letter-spacing:1px;line-height:1}

/* Nav */
.nav{position:absolute;top:620px;left:0;width:1200px;height:66px;background:var(--brown);display:flex;align-items:center;padding:0 24px}
.nav ul{list-style:none;display:flex}
.nav li{color:#efe6d8;font-size:14px;padding:0 20px;border-right:1px solid #5a4838}
.nav li:first-child{padding-left:0}
.nav .cta{margin-left:auto;background:var(--cream);color:var(--brown);font-size:14px;font-weight:500;padding:10px 22px;display:flex;align-items:center;gap:10px}

/* Concept */
.concept{position:absolute;top:686px;left:0;width:1200px;height:614px;background:var(--paper);text-align:center}
.concept .small-logo{margin:40px auto 0;display:flex;align-items:center;justify-content:center;gap:8px}
.concept .small-logo .mark{width:12px;height:12px;border-radius:50%;background:var(--gold)}
.concept .small-logo span{font-family:"Noto Serif JP",serif;font-weight:700;font-size:16px;color:var(--gold-dark)}
.section-title{font-size:32px;font-weight:400;letter-spacing:1px;margin-top:6px}
.rule{width:420px;height:1px;background:#cbbca8;margin:14px auto 0}
.concept .lead{font-family:"Noto Serif JP",serif;font-weight:700;font-size:21px;margin-top:40px;letter-spacing:1px}
.concept p{font-size:13px;line-height:2;color:#4d4036;margin-top:26px}

/* News */
.news{position:absolute;top:1300px;left:0;width:1200px;height:210px;background:var(--brown);color:#eee4d5}
.news .section-title{text-align:center;color:var(--white);margin-top:14px;font-size:28px}
.news .rule{background:#6c5a49;width:900px;margin-top:8px}
.news ul{list-style:none;width:880px;margin:12px auto 0}
.news li{display:flex;gap:22px;font-size:12px;padding:6px 0;border-bottom:1px dotted #5c4a3b}
.news .date{color:#c9b9a3;width:90px}
.news .cat{color:var(--gold);width:70px}

/* Gallery */
.gallery{position:absolute;top:1510px;left:0;width:1200px;height:590px;background:var(--paper)}
.ribbon{position:absolute;top:24px;left:420px;width:360px;height:46px;background:var(--red);color:var(--white);font-size:22px;font-weight:500;text-align:center;line-height:46px;letter-spacing:1px}
.feature{position:absolute;top:100px;left:30px;width:370px;height:230px;background:linear-gradient(135deg,#efe8de,#c9b49a 60%,#9c8266)}
.feature-cap{position:absolute;top:340px;left:30px;width:370px;text-align:center;font-size:11px;color:var(--muted)}
.grid{position:absolute;top:100px;left:450px;width:690px;display:grid;grid-template-columns:repeat(4,1fr);gap:8px}
.grid .photo{height:78px}
.arrow{position:absolute;top:190px;width:28px;height:48px;background:var(--brown);display:flex;align-items:center;justify-content:center}
.arrow.prev{left:414px}
.arrow.next{left:1150px}
.more-btn{position:absolute;top:460px;left:400px;width:400px;height:62px;background:var(--gold);color:var(--brown);font-size:17px;text-align:center;line-height:62px;letter-spacing:1px}

/* Social feed placeholder */
.feed{position:absolute;top:2110px;left:22px;width:1156px;height:260px;background:var(--blue);color:var(--white);font-size:40px;display:flex;align-items:center;justify-content:center}

/* Footer */
.footer{position:absolute;top:2380px;left:0;width:1200px;height:120px;background:var(--cream);border-top:3px solid var(--brown)}
.f-tel{position:absolute;left:30px;top:8px}
.f-label{display:inline-block;background:var(--brown);color:var(--white);font-size:10px;padding:2px 10px}
.f-tel .num{font-size:32px;font-weight:700;color:var(--brown);letter-spacing:1px;line-height:1.2}
.f-tel .hours{font-size:10px;color:var(--muted)}
.f-mail{position:absolute;left:380px;top:8px}
.f-mail .addr{display:flex;align-items:center;gap:10px;font-size:22px;font-weight:500;color:var(--brown);background:var(--white);border:1px solid #d9cdbb;padding:6px 14px;margin-top:4px}
.f-info{position:absolute;left:800px;top:10px;font-size:10px;line-height:1.7;color:#5b4c40}
.f-logo{position:absolute;right:24px;top:12px;width:130px;height:64px;background:var(--brown);display:flex;align-items:center;justify-content:center;gap:8px}
.f-logo .mark{width:12px;height:12px;border-radius:50%;background:var(--gold)}
.f-logo span{font-family:"Noto Serif JP",serif;font-weight:700;font-size:18px;color:var(--white)}
.copy{position:absolute;bottom:0;left:0;width:1200px;height:20px;background:var(--brown);color:#cbbda9;font-size:10px;text-align:center;line-height:20px}
</style>
</head>
<body>

<header>
  <div class="topbar">自然素材で建てる、暮らしが楽しい住まい</div>
  <div class="hero" role="img" aria-label="白い外壁と黒い屋根の二階建て住宅の外観写真"></div>
  <div class="logo-box"><div class="mark"></div><div class="name">Tovaru</div></div>
  <div class="tel-box">
    <svg width="22" height="22" viewBox="0 0 24 24" fill="#d8b46a"><path d="M6.6 10.8a15.1 15.1 0 0 0 6.6 6.6l2.2-2.2a1 1 0 0 1 1-.25 11.4 11.4 0 0 0 3.6.57 1 1 0 0 1 1 1V20a1 1 0 0 1-1 1A17 17 0 0 1 3 4a1 1 0 0 1 1-1h3.5a1 1 0 0 1 1 1c0 1.25.2 2.45.57 3.6a1 1 0 0 1-.25 1z"/></svg>
    <div><div class="label">お問い合わせ・資料請求</div><div class="num">0120-48-7316</div></div>
  </div>
</header>

<nav class="nav">
  <ul>
    <li>家づくり</li><li>建築事例</li><li>お問い合わせ</li><li>資料請求</li><li>会社概要</li>
  </ul>
  <div class="cta">資料請求はこちら
    <svg width="10" height="12" viewBox="0 0 10 12"><path d="M1 1l7 5-7 5z" fill="#2b1f18"/></svg>
  </div>
</nav>

<section class="concept">
  <div class="small-logo"><div class="mark"></div><span>Tovaru</span></div>
  <h2 class="section-title">Brand Concept</h2>
  <div class="rule"></div>
  <p class="lead">「自然が持つ美しさ」と「暮らす人の思い」を取り入れ『生活が楽しい住まい』を創ります。</p>
  <p>人々に永く愛されてきた天然素材を使用することで自然素材だけが持つ色や質感から<br>
  確かな手触りと温もりを暮らす人に与え続けてくれます。<br>
  新しいだけを追い過ぎず自然素材の持つ機能性を生かして自然の働きでしっかりと家を守る<br>
  それは流行に左右されない気品を保つ「素朴で美しい風合い」に仕上がります。</p>
  <p>住む人のライフスタイルや好みをしっかりとお聞かせいただいた上で土地を生かし<br>
  隣地環境と調和のある設計を企画し、その人らしい家を一緒に考えていきます。</p>
  <p>それはその人がどんなふうに暮らしていきたいのかを一緒に考え、その地で永く暮らしていく<br>
  イメージを膨らませ生活が楽しくなる様な空間を提案します。</p>
</section>

<section class="news">
  <h2 class="section-title">News&amp;Topics</h2>
  <div class="rule"></div>
  <ul>
    <li><span class="date">2014.00.00</span><span class="cat">施工事例</span><span>無垢材と漆喰で仕上げた平屋の施工事例を公開しました。</span></li>
    <li><span class="date">2014.00.00</span><span class="cat">イベント</span><span>自然素材の家を体感できる完成見学会を開催いたします。</span></li>
    <li><span class="date">2014.00.00</span><span class="cat">お知らせ</span><span>夏季休業期間のお問い合わせ対応についてのご案内です。</span></li>
    <li><span class="date">2014.00.00</span><span class="cat">施工事例</span><span>薪ストーブのある二階建て住宅の事例を追加しました。</span></li>
  </ul>
</section>

<section class="gallery">
  <h2 class="ribbon">Tovaru Garelly</h2>
  <div class="feature" role="img" aria-label="木の床と白い壁の明るいリビングの室内写真"></div>
  <p class="feature-cap">自然素材に囲まれた明るい住まい</p>
  <div class="arrow prev"><svg width="10" height="14" viewBox="0 0 10 14"><path d="M8 1L2 7l6 6" stroke="#fff" stroke-width="2" fill="none"/></svg></div>
  <div class="grid">
    <div class="photo" role="img" aria-label="室内の写真" style="background:linear-gradient(135deg,#f1ebe2,#b99d7d)"></div>
    <div class="photo" role="img" aria-label="キッチンの写真" style="background:linear-gradient(135deg,#e8e2d8,#8f7a64)"></div>
    <div class="photo" role="img" aria-label="住宅外観の写真" style="background:linear-gradient(180deg,#a9bfd2,#dcd6cc 55%,#6d6a5c)"></div>
    <div class="photo" role="img" aria-label="木製ドアの写真" style="background:linear-gradient(135deg,#d9cdbd,#7a5a3e)"></div>
    <div class="photo" role="img" aria-label="和室の写真" style="background:linear-gradient(135deg,#e9dfcd,#a88c65)"></div>
    <div class="photo" role="img" aria-label="階段の写真" style="background:linear-gradient(135deg,#f3eee6,#9d8468)"></div>
    <div class="photo" role="img" aria-label="住宅外観の写真" style="background:linear-gradient(180deg,#b5c6d4,#e4ddd2 55%,#7a7463)"></div>
    <div class="photo" role="img" aria-label="玄関の写真" style="background:linear-gradient(135deg,#e4d8c7,#8b6d4f)"></div>
    <div class="photo" role="img" aria-label="ウッドデッキの写真" style="background:linear-gradient(135deg,#cbb89d,#6f5540)"></div>
    <div class="photo" role="img" aria-label="洗面室の写真" style="background:linear-gradient(135deg,#f4f0ea,#b5a189)"></div>
    <div class="photo" role="img" aria-label="寝室の写真" style="background:linear-gradient(135deg,#ede4d6,#9e8a74)"></div>
    <div class="photo" role="img" aria-label="庭と外構の写真" style="background:linear-gradient(180deg,#c7d2d9,#a8ab8c 60%,#6b6b4f)"></div>
  </div>
  <div class="arrow next"><svg width="10" height="14" viewBox="0 0 10 14"><path d="M2 1l6 6-6 6" stroke="#fff" stroke-width="2" fill="none"/></svg></div>
  <div class="more-btn">建築事例の詳細はこちら</div>
</section>

<section class="feed">Social Feed Area</section>

<footer class="footer">
  <div class="f-tel">
    <span class="f-label">お電話でのお問い合わせ</span>
    <div class="num">0120-48-7316</div>
    <div class="hours">受付時間 9:00〜18:00（水曜定休）</div>
  </div>
  <div class="f-mail">
    <span class="f-label">メールでのお問い合わせ</span>
    <div class="addr">
      <svg width="26" height="20" viewBox="0 0 26 20"><rect x="1" y="1" width="24" height="18" fill="none" stroke="#2b1f18" stroke-width="2"/><path d="M1 1l12 10L25 1" fill="none" stroke="#2b1f18" stroke-width="2"/></svg>
      info@tovaru-home.jp
    </div>
  </div>
  <div class="f-info">
    株式会社トヴァル<br>
    〒000-0000 長野県○○市中央1-2-3<br>
    ファクス 0120-48-7317<br>
    営業時間 9:00〜18:00 定休日 水曜日
  </div>
  <div class="f-logo"><div class="mark"></div><span>Tovaru</span></div>
  <div class="copy">Copyright (C) Tovaru Home Co., Ltd. All Rights Reserved.</div>
</footer>

</body>
</html>
```